Business Card for Quillmark Ledger - A cannabis publication for executives.

I'd like some business cards for Quillmark Ledger. The logo is done (great job!) and I need a card design I will use with PRINTLY. I made it a short project to allow time for printing before an event. These will be standard sized cards (final artwork size 3.66" x 2.16" at 300dpi) with a final card size of 3.5" x 2.0". (See PRINTLY.com if you need more info.) I might try rounded corners but am not sure yet. I think the design will work okay with rounded.

Quillmark Ledger will be a bi-weekly publication for the cannabis industry. It is targeted to investors and industry executives, not consumers or pot smokers. So our market is more B2B. However I am open to creativity and making the card something people remark on.

My contact for card:

Dana Merrow
Founder/CEO
dana@quillmarkledger.example

2740 Harlow Avenue
Boston MA 02135
(617)555-0194

Target Market(s)

Executives, Industry people and investors in the Cannabis sector.

Contact Information for Business Card

PRINTLY does do double sided and the second side can be the same or different images. Only one side is required but use of the second side would be a bonus.

Font styles to use
Serif
Sans Serif
Decorative

Colors

Designer to choose colors to be used in the design.

Requirements
Must have
• Logo, contact info
Nice to have
• Style and design to make the card stand out in a crowd.

```html
<!DOCTYPE html>
<html lang="en">
<head>
<meta charset="UTF-8">
<title>Quillmark Ledger – Business Card</title>
<link rel="stylesheet" href="https://fonts.googleapis.com/css2?family=Open+Sans:wght@400;600;700&display=swap">
<style>
  :root {
    --backdrop: #1b1b1b;
    --card: #2a2a2a;
    --card-edge: #333333;
    --ink-white: #f2f2f2;
    --ink-grey: #cfcfcf;
    --ink-muted: #bdbdbd;
    --rule: #6a6a6a;
    --brand-green: #7ab62e;
    --brand-blue: #2f80c9;
    --front-mark: #3a3a3a;
  }
  * { box-sizing: border-box; margin: 0; padding: 0; }
  html, body { width: 1200px; height: 1000px; overflow: hidden; }
  body {
    background: var(--backdrop);
    font-family: "Open Sans", Arial, sans-serif;
    position: relative;
  }
  .card {
    position: absolute;
    left: 280px;
    width: 640px;
    height: 366px;
    background: var(--card);
    border: 1px solid var(--card-edge);
    box-shadow: 0 18px 40px rgba(0,0,0,0.55);
  }
  .card--front { top: 104px; display: flex; align-items: center; justify-content: center; }
  .card--back { top: 530px; }

  .front-brand { display: flex; align-items: center; gap: 22px; }
  .front-brand__square { width: 58px; height: 58px; background: var(--front-mark); }
  .front-brand__name { font-size: 44px; font-weight: 600; color: var(--ink-grey); letter-spacing: 0.5px; }

  .back-brand {
    position: absolute; left: 46px; top: 118px; width: 190px;
    display: flex; flex-direction: column; align-items: flex-start; gap: 14px;
  }
  .back-brand__circle { width: 40px; height: 40px; border-radius: 50%; background: var(--brand-green); }
  .back-brand__name { font-size: 28px; line-height: 1.15; font-weight: 700; color: var(--brand-green); }

  .divider { position: absolute; left: 262px; top: 96px; width: 3px; height: 176px; background: var(--rule); }

  .contact { position: absolute; left: 290px; top: 94px; color: var(--ink-muted); }
  .contact__name { font-size: 25px; font-weight: 700; letter-spacing: 0.5px; line-height: 1.1; }
  .contact__first { color: var(--brand-blue); }
  .contact__last { color: var(--brand-green); }
  .contact__title { font-size: 15px; font-weight: 600; color: var(--ink-white); margin-top: 2px; }
  .contact__address { font-size: 15px; line-height: 1.3; margin-top: 12px; }
  .contact__lines { list-style: none; margin-top: 12px; font-size: 15px; line-height: 1.55; }
  .contact__lines li { display: flex; align-items: center; gap: 12px; }
  .contact__lines svg { width: 13px; height: 13px; flex: none; }
  .contact__domain { color: var(--brand-green); }
</style>
</head>
<body>
  <section class="card card--front" aria-label="Card front">
    <div class="front-brand">
      <span class="front-brand__square"></span>
      <span class="front-brand__name">Quillmark Ledger</span>
    </div>
  </section>

  <section class="card card--back" aria-label="Card back">
    <div class="back-brand">
      <span class="back-brand__circle"></span>
      <span class="back-brand__name">Quillmark<br>Ledger</span>
    </div>
    <div class="divider"></div>
    <div class="contact">
      <p class="contact__name"><span class="contact__first">Dana</span> <span class="contact__last">Merrow</span></p>
      <p class="contact__title">Founder/CEO</p>
      <p class="contact__address">2740 Harlow Avenue,<br>Boston MA 02135</p>
      <ul class="contact__lines">
        <li>
          <svg viewBox="0 0 24 24" aria-hidden="true"><path fill="#7ab62e" d="M6.6 10.8a15 15 0 0 0 6.6 6.6l2.2-2.2a1 1 0 0 1 1-.25 11.4 11.4 0 0 0 3.6.57 1 1 0 0 1 1 1V20a1 1 0 0 1-1 1A17 17 0 0 1 3 4a1 1 0 0 1 1-1h3.5a1 1 0 0 1 1 1c0 1.25.2 2.45.57 3.57a1 1 0 0 1-.25 1z"/></svg>
          <span>(617)555-0194</span>
        </li>
        <li>
          <svg viewBox="0 0 24 24" aria-hidden="true"><rect x="2" y="5" width="20" height="14" fill="#7ab62e"/><path d="M2 5l10 8 10-8" fill="none" stroke="#2a2a2a" stroke-width="2"/></svg>
          <span>dana@quillmarkledger.example</span>
        </li>
        <li>
          <svg viewBox="0 0 24 24" aria-hidden="true"><circle cx="12" cy="12" r="10" fill="#7ab62e"/><path d="M2 12h20M12 2v20M5 6.5h14M5 17.5h14" stroke="#2a2a2a" stroke-width="1.4" fill="none"/></svg>
          <span>www.<span class="contact__domain">quillmarkledger</span>.example</span>
        </li>
      </ul>
    </div>
  </section>
</body>
</html>
```